Major Australian Food and Wine Event Web Design Project

The project will consist of 3 designs
The homepage
A city hub page
A general content page

The main audience who will visit the website will be (in Order of importance:

1) Visitors
- Mainly women 24 – 54 years (they are the main ticket buyers)
- In a relationship – so will go to the show with their partner
- In a good paying job or home maker – and who have disposable income to spend $30 a ticker
- Enjoy food, wine and going out
- Looking for a fun day out – although an event that is about food and wine – it is an event that most people will go to and have a fun day out – not too pretentious

A smaller proportion of the audience will be:
2) Exhibitors & sponsors ( both prospective and existing)
3) Media

Objectives:

- Functionality on home page and sub pages needs to be updated, clear, easy to navigate and inject a sense of ‘fun’ – need to make it look more professional
- Need to incorporate the many things that need to be on the home page and sub pages in a visually appealing manner
- Ensure the ‘Cons’ above are considered and reflected in functionality and design
- To not be too focus on the colours (these can be changed) – but focus on the functionality and overall design opportunities.

Approach:

Keywords to describe the Bright Plate & Vine Fair:
Fun day out, discover, learn, indulge, entertaining

Other website examples:

Some great consumers event websites from the UK really make our website look basic and juvenile – and below are some examples of the presentation of how we would like our website to look like:

http://www.morselfairs-example.com/london/ This website is clean, includes good social media integration and exudes a sense of fun. Their content pages, such as the features landing page also presents options in a clear and visually appealing way with a series of boxes including image and text http://www.morselfairs-example.com/london/content/343/Features

http://www.homecraftexpo-example.com/ - this is also a great website – and it incorporates all the elements we would be looking for on our homepage – but the background/skin also includes a sense of fun and cheekiness. Subpages also are consistent.

Features

• Its a fun day that offers great value for money
• Caters to all visitors, regardless of different levels of knowledge or interest in food, wine and cooking.
• Sample great quality food and wine products from hundreds of reputable exhibitors
• Learn more through many of the shows feature activities (Celeb Theatre, Wine Theatre, Cooking & Cheese Classes)

Functionality & Structure:

In a user friendly, easy to view way, we need to incorporate the following functionality elements on home page:
- main header (that will incorporate our current creative) with a ‘fun’ skin
- navigation tabs/references (hone, location, tickets, blog, sign up, exhibitors)
- navigation/content banner (rotating)
- Area for small intro about the show
- News and highlight section
- New exhibitors section
- Obvious Ticket call to action
- Obvious sign up call to action
- Social media buttons or links ( really like the moving gifs on the Homecraftexpo-example.com site
- area for advertising (MREC size) to sell to exhibitors/sponsors
- Show dates for all 5 shows (maybe in main header)

Subpage layout is also important and needs to reflect the homepage – so would also like to see examples of how this would look and tie in with navigation – we generally have a lot of content on these pages, so clear navigation would be useful. – see below for further details of functionality for city Hubs

‘CITY HUB’ BRIEF
When navigating to each location the user will be taken to a ‘CITY HUB’ which should replicate design and content elements of a main HOME page, as well as reflect more specific information for each Show. Elements which must appear on this page are:
• FEATURES – which may be displayed in categories (in boxes, see appendix 1.0) which will link through to relevant content pages. Or in one box which will link through to a features page with all presented in boxes
• CHEFS – may be displayed as a separate icon box which will link to chefs page with bios, Celeb Theatre timetable etc.
• TICKETS – either a button or clear callout to purchase tickets
• PLAN YOUR DAY – may be displayed in a separate content box which will then link through to getting there, sample itineraries and downloadable pocket show guide for visitors to print before coming to the Show.
• WHO’S EXHIBITING – to link back to city specific exhibitor lists

Our current website is out of date and has the following inadequacies (www.brightplatefair-example.com.au) -

The homepage
A city hub page
A general content page

1) Visitors

3) Media

Objectives:

Approach:

To be perceived as a fun, entertaining event with something for everyone - website creative and navigation must reflect this.

Other website examples:

Features

- New exhibitors section

‘CITY HUB’ BRIEF

- Dated design/layout
- Homepage too text heavy
- No content boxes that can be used for different features/areas (eg. News, Exhibitors etc)
- Uninspiring colours and skin(eg. grey background), does not reflect ‘a fun day out’
- Limited presence of social media platforms and lacks ‘community’
- No continuity in sub pages
- main banner too big – takes up too much space on homepage

Requirements
Must have
• As per above brief.

In addition:
Floating social media buttons on side
Wrap around image
Drop down menu (specifically for the location nav item)

```html
<!DOCTYPE html>
<html lang="en">
<head>
<meta charset="utf-8">
<title>Bright Plate &amp; Vine Fair</title>
<link rel="stylesheet" href="https://fonts.googleapis.com/css2?family=Poiret+One&family=Open+Sans:wght@400;600;700&family=PT+Sans:wght@400;700&display=swap">
<style>
:root{
  --red:#c8100f;
  --red-dark:#8c0606;
  --gold:#b59a4f;
  --gold-dark:#8e7630;
  --olive:#8a7418;
  --ink:#222;
  --grey-bg:#e6e6e6;
  --footer:#464646;
  --footer-text:#ddd;
  --lime:#b7c43c;
  --orange:#e0901c;
  --blue:#1a6ec8;
}
*{box-sizing:border-box;margin:0;padding:0}
html,body{width:1024px;height:1200px;overflow:hidden}
body{position:relative;background:linear-gradient(#fff 0,#fff 430px,#d9d9d9 470px,#f2f2f2 980px);font-family:"Open Sans",Arial,sans-serif;color:var(--ink)}
.abs{position:absolute}
/* header */
.topbar{left:0;top:20px;width:1024px;height:53px;background:linear-gradient(#e02020,#b00808);box-shadow:0 4px 6px rgba(0,0,0,.25)}
.brand{left:119px;top:0;width:148px;height:111px;background:#fff;box-shadow:0 0 6px rgba(0,0,0,.3);display:flex;align-items:center;justify-content:center;gap:6px;padding:6px}
.brand span{font-family:"Open Sans",sans-serif;font-weight:700;font-size:15px;line-height:1.15;color:var(--red);text-align:center}
.brand i{width:12px;height:12px;border-radius:50%;background:var(--red);flex:none}
.nav{left:326px;top:20px;height:53px;display:flex}
.nav a{display:block;padding:0 18px;line-height:53px;color:#fff;font-size:9.5px;letter-spacing:.6px;text-decoration:none;border-right:1px solid rgba(0,0,0,.2)}
.nav a.active{background:#a90505;padding:0 26px}
.search{left:765px;top:36px;width:147px;height:18px;border-radius:9px;background:#9c0707;box-shadow:inset 0 1px 3px rgba(0,0,0,.5)}
.search svg{position:absolute;right:8px;top:3px}
.follow{left:918px;top:80px;width:31px;height:104px}
/* banner */
.banner{left:0;top:111px;width:1024px;height:310px;background:radial-gradient(ellipse at 50% 40%,#c9ae63,#a88e45)}
.bandline{left:0;top:414px;width:1024px;height:18px;background:linear-gradient(#e6c640 0,#e6c640 4px,#d11010 4px,#a80808 14px,#ddd 14px)}
.hero-title{font-family:"Poiret One",sans-serif;color:#fff;text-shadow:0 2px 3px rgba(0,0,0,.4)}
.t1{left:175px;top:142px;font-size:40px}
.t2{left:211px;top:189px;font-size:30px;word-spacing:16px}
.t3{left:236px;top:218px;font-size:54px}
.teaser{left:171px;top:307px;width:330px;height:67px;border:1px solid #d7c458;background:rgba(150,125,50,.35);padding:6px 27px}
.teaser p{font-family:"Poiret One",sans-serif;font-size:20px;color:#fff}
.teaser strong{display:block;font-family:"PT Sans",sans-serif;font-weight:400;font-size:16.5px;color:#b00808;letter-spacing:.3px;margin-top:4px}
.hero-photo{left:425px;top:143px;width:446px;height:253px;border:3px solid #888;border-radius:3px;background:radial-gradient(circle at 55% 50%,#c0392b,#e0a43a 35%,#9fbf6a 70%,#dfe8c8)}
/* intro */
.intro-h{left:119px;top:447px;font-family:"Poiret One",sans-serif;font-size:25px;color:#222}
.intro-h em{font-style:normal;font-family:"Open Sans",sans-serif;font-size:15px;color:var(--olive)}
.intro{left:121px;top:487px;width:500px;font-size:9.2px;line-height:1.35}
.intro p{margin-bottom:10px}
.cta{top:596px;width:220px;text-align:center}
.cta p{color:var(--olive);font-size:13px;margin-bottom:12px}
.btn{display:inline-block;width:176px;height:34px;line-height:34px;background:linear-gradient(#e01818,#a50606);color:#fff;font-family:"PT Sans",sans-serif;font-size:17px;box-shadow:0 3px 4px rgba(0,0,0,.35);border-radius:2px}
.divider{top:575px;width:2px;height:130px;background:linear-gradient(transparent,#bbb,transparent)}
/* boxes */
.box{top:716px;width:250px;height:228px;background:#fff;border:1px solid #ddd;box-shadow:0 1px 4px rgba(0,0,0,.2);border-radius:3px}
.box.news{left:119px;background:linear-gradient(#fff,#f8dede)}
.box.exh{left:385px;background:linear-gradient(#fff,#ddd)}
.box h3{position:absolute;left:20px;top:18px;font-weight:600;font-size:12.5px;color:var(--olive);letter-spacing:.3px}
.box .rule{position:absolute;left:20px;right:22px;top:38px;height:1px;background:#ccc}
.box .ico{position:absolute;right:32px;top:13px;width:26px;height:20px;background:var(--olive);border-radius:2px}
.news-body{position:absolute;left:27px;top:50px;width:200px;font-size:9.3px;line-height:1.3}
.news-body b{font-size:9.3px}
.news-body .date{color:var(--orange);margin:3px 0 5px;display:block}
.more{position:absolute;font-style:italic;color:#b00808;font-size:9.5px}
.viewall{position:absolute;right:30px;bottom:20px;font-size:9.5px;color:var(--olive);text-decoration:underline}
.viewall:before{content:"\25B6";text-decoration:none;display:inline-block;margin-right:8px;font-size:8px}
.circle{position:absolute;top:53px;width:17px;height:17px;border-radius:50%;background:#777}
.exh-photo{position:absolute;left:17px;top:48px;width:210px;height:100px;background:linear-gradient(135deg,#6e5b4c,#b78a6a 45%,#8d3a2a 75%,#4a4a5a)}
.exh-text{position:absolute;left:18px;top:155px;width:210px;font-size:9.3px;font-weight:600;line-height:1.3;color:#333}
/* right column */
.ad{left:672px;top:454px;width:247px;height:164px;background:#aee0f0;text-align:center;color:#222;padding-top:18px;font-family:"Open Sans",sans-serif}
.ad .a1{font-weight:700;font-size:40px;line-height:.95;letter-spacing:-1px}
.ad .a2{font-size:37px;line-height:1;letter-spacing:-1px}
.ad .a3{color:var(--blue);font-weight:700;font-size:20px;border-bottom:2px solid #222;margin:0 30px 4px;padding-bottom:2px}
.ad .a4{font-weight:700;font-size:23px}
.newsletter{left:669px;top:631px;width:250px;height:202px;background:linear-gradient(#fff,#e4e4e4);box-shadow:0 1px 5px rgba(0,0,0,.25);border-radius:3px}
.newsletter .l1{position:absolute;left:19px;top:16px;font-size:14px;color:#333}
.newsletter .l2{position:absolute;left:21px;top:36px;font-size:16px;font-weight:700;letter-spacing:1px;color:#333}
.newsletter .well{position:absolute;left:20px;top:63px;width:211px;height:72px;background:#c9c9c9}
.newsletter .field{position:absolute;left:13px;top:12px;width:184px;height:22px;background:#fff;border:1px solid #aaa}
.newsletter .sub{position:absolute;left:13px;top:42px;width:92px;height:23px;line-height:23px;text-align:center;background:linear-gradient(#8f7a28,#5e4e12);color:#fff;font-weight:700;font-size:10.5px}
.newsletter .copy{position:absolute;left:22px;top:155px;width:215px;font-size:9.2px;line-height:1.3}
.tweets{left:669px;top:847px;width:250px;height:115px;background:#fff;border:1px solid #ccc}
.tweets h4{position:absolute;left:7px;top:8px;font-size:14px;font-weight:400}
.tweets h4 b{color:var(--blue)}
.tweets .birds{position:absolute;right:12px;top:6px;width:104px;height:62px;background:radial-gradient(ellipse,#3fa0e0,#bde2f7 70%,#fff);border-radius:40%}
.tweets .txt{position:absolute;left:9px;top:34px;width:236px;font-size:9.3px;line-height:1.3}
.tweets .txt span{color:#b00808}
.tweets .see{position:absolute;right:13px;bottom:5px;font-size:9.3px;font-style:italic;text-decoration:underline;color:var(--olive)}
.shadowline{left:130px;top:970px;width:765px;height:6px;background:radial-gradient(ellipse,#555 0,transparent 70%)}
/* footer */
.footer{left:119px;top:992px;width:800px;height:162px;background:var(--footer);color:var(--footer-text)}
.footer .fh{position:absolute;left:27px;top:12px;color:var(--lime);font-size:13px}
.footer .fd{position:absolute;left:27px;top:36px;width:205px;font-size:8px;line-height:1.15}
.footer .tel{position:absolute;left:27px;font-size:11px}
.footer .tel b{color:var(--lime);font-weight:400;font-size:14px}
.footer .lh{position:absolute;left:283px;top:12px;color:var(--lime);font-size:10.5px}
.links{position:absolute;top:34px;list-style:none;font-size:9.3px;line-height:13px}
.links li:before{content:"";display:inline-block;width:5px;height:5px;border-radius:50%;background:#aaa;margin-right:10px;vertical-align:middle}
.links li.hl{color:var(--orange)}
.contact{position:absolute;left:564px;top:10px;width:200px;height:30px;line-height:30px;background:#3a3a3a;box-shadow:2px 3px 4px rgba(0,0,0,.5);color:#fff;font-size:12.5px;font-weight:600;padding-left:15px}
.footer label{position:absolute;left:570px;font-size:9px}
.footer .in{position:absolute;left:613px;width:135px;height:18px;background:#5a5a5a;border:1px solid #777}
.send{position:absolute;left:692px;top:118px;width:74px;height:21px;line-height:21px;text-align:center;background:linear-gradient(#bfa12e,#8a7012);color:#fff;font-weight:700;font-size:11px}
.copyright{left:0;top:1153px;width:1024px;height:47px;background:#000;color:#fff;font-family:Arial,sans-serif;font-size:9.5px;padding:16px 0 0 141px}
</style>
</head>
<body>
<header>
  <div class="abs topbar"></div>
  <div class="abs brand"><i></i><span>Bright Plate<br>&amp; Vine Fair</span></div>
  <nav class="abs nav">
    <a class="active" href="#">HOME</a>
    <a href="#">WANT TO EXHIBIT?</a>
    <a href="#">RECIPE CLUB</a>
    <a href="#">NEWS AND MEDIA</a>
  </nav>
  <div class="abs search"><svg width="11" height="11" viewBox="0 0 11 11"><circle cx="4" cy="4" r="3" fill="none" stroke="#fff" stroke-width="1.6"/><line x1="6.3" y1="6.3" x2="10" y2="10" stroke="#fff" stroke-width="2"/></svg></div>
  <svg class="abs follow" viewBox="0 0 31 104"><path d="M0 0 L31 18 V98 L0 104 Z" fill="#b30808"/><path d="M0 0 L31 18 V24 L0 6Z" fill="#7a0404"/><text x="20" y="85" transform="rotate(-90 20 85)" fill="#fff" font-size="8" font-family="Open Sans,sans-serif" letter-spacing=".5">FOLLOW US ▸</text></svg>
</header>

<section class="abs banner" aria-label="Rotating banner">
</section>
<svg class="abs" style="left:116px;top:236px" width="36" height="58"><polyline points="34,1 2,29 34,57" fill="none" stroke="#6e5a20" stroke-width="1.2"/></svg>
<svg class="abs" style="left:886px;top:236px" width="36" height="58"><polyline points="2,1 34,29 2,57" fill="none" stroke="#6e5a20" stroke-width="1.2"/></svg>
<div class="abs hero-title t1">Succumb</div>
<div class="abs hero-title t2">To Your</div>
<div class="abs hero-title t3">Senses</div>
<div class="abs hero-photo" role="img" aria-label="Plate of nachos with melted cheese and salsa"></div>
<div class="abs teaser"><p>Delight your palate at a</p><strong>CURDCRAFT DISCOVERY CLASS</strong></div>
<div class="abs bandline"></div>

<main>
  <h1 class="abs intro-h" style="font-weight:400">The Bright Plate &amp; Vine Fair <em>- all over for another year!</em></h1>
  <div class="abs intro">
    <p>What a year for good food and wine!</p>
    <p>Melbourne, Sydney, Perth, Adelaide and Brisbane have all had the chance to experience the fun, excitement and joy, that is the Bright Plate &amp; Vine Fair!</p>
    <p>We would like to thank all our amazing visitors for coming along and helping us celebrate another awesome year - &nbsp;A big thank you also to the rest of the crew including exhibitors, sponsors and chefs!</p>
  </div>
  <div class="abs divider" style="left:357px"></div>
  <div class="abs divider" style="left:632px"></div>
  <div class="abs cta" style="left:124px"><p>To buy a ticket contact us here!</p><span class="btn">BUY A TICKET</span></div>
  <div class="abs cta" style="left:392px"><p>To book a stand contact us here!</p><span class="btn">BOOK A STAND</span></div>

  <article class="abs box news">
    <h3>NEWS AND HIGHTLIGHTS</h3><span class="ico"></span><span class="rule"></span>
    <span class="circle" style="left:5px"></span><span class="circle" style="right:3px"></span>
    <div class="news-body">
      <b>Move Over Pavlova, the Aussie BBQ is King!</b>
      <span class="date">June 2010</span>
      The traditional Aussie BBQ has been voted Australia's most iconic dish by more than 50 percent of Australians, followed by the humble meat pie and sauce (16 per cent), with 12 percent believing a good old roast dinner deserves top spot..
    </div>
    <span class="more" style="right:27px;top:170px">read more</span>
    <span class="viewall">VIEW ALL</span>
  </article>

  <article class="abs box exh">
    <h3>EXHIBITORS</h3><span class="ico"></span><span class="rule"></span>
    <div class="exh-photo" role="img" aria-label="Visitors tasting wine at an exhibitor stand"></div>
    <svg style="position:absolute;right:-3px;top:50px" width="14" height="34"><polyline points="2,9 7,4 12,9" fill="none" stroke="#333"/><polyline points="2,25 7,30 12,25" fill="none" stroke="#333"/></svg>
    <p class="exh-text">They're eager, enthusiastic and actively looking for new tastes and ideas,</p>
    <span class="viewall">VIEW ALL</span>
  </article>
</main>

<aside>
  <div class="abs ad" role="img" aria-label="Sponsor advertisement">
    <div class="a1">HOMECRAFT</div><div class="a2">EXPO</div><div class="a3">AWARDS 2012</div><div class="a4">ENTER NOW</div>
  </div>
  <div class="abs newsletter">
    <span class="l1">Subscribe to our</span><span class="l2">FREE NEWSLETTER</span>
    <div class="well"><span class="field"></span><span class="sub">Subscribe</span></div>
    <p class="copy">Get our free newsletter and keep up to date with the events and happenings of The Bright Plate &amp; Vine Fair!</p>
  </div>
  <div class="abs tweets">
    <h4>ON <b>CHIRPLINE</b>:</h4>
    <div class="birds" role="img" aria-label="Two cartoon blue birds"></div>
    <p class="txt"><span>2 hours ago</span><br>@Millbrookfarm Was delicious,<br>v.rich &amp; meaty! Had tried<br>before @MorselLondon but<br>great to see top quality in mainstream restaurant!</p>
    <span class="see">See More</span>
  </div>
</aside>

<div class="abs shadowline"></div>

<footer class="abs footer">
  <span class="fh">Bright Plate And Vine Fair</span>
  <p class="fd">taste your way around the event and discover delicious food and wine products from a host of regional producers and exciting exhibitors.</p>
  <p class="tel" style="top:92px">Toll Free: <b>555-555-5555</b></p>
  <p class="tel" style="top:109px">To Order: <b>555-555-5555</b></p>
  <span class="lh">Site Links:</span>
  <ul class="links" style="left:283px"><li>Home</li><li>Melbourne</li><li>Sydney</li><li>Perth</li><li>Adelaide</li><li>Brisbane</li><li class="hl">Privacy Policy</li></ul>
  <ul class="links" style="left:402px"><li>Want to exhibit?</li><li>Recipe club</li><li>News and Media</li><li>Sponsors</li><li>Exhibitor information</li><li>Contact us</li><li class="hl">Disclaimer</li></ul>
  <div class="contact">Have A Question? Contact Us</div>
  <label style="top:64px">Name:</label><span class="in" style="top:62px"></span>
  <label style="top:88px">Email:</label><span class="in" style="top:86px"></span>
  <span class="send">SEND</span>
</footer>
<div class="abs copyright">Copyright &nbsp;© &nbsp;2012 BRIGHT PLATE AND VINE FAIR. All Rights Reserved.</div>
</body>
</html>
```